K9R Business Cards

Business Cards

Contact Information for Business Card

Company name, owner name, license #s, phone & email

Requirements
Should not have
• mailing address

```html
<!DOCTYPE html>
<html lang="en">
<head>
<meta charset="UTF-8">
<title>K9R Construction Business Cards</title>
<link href="https://fonts.googleapis.com/css2?family=Open+Sans:wght@400;700;800&display=swap" rel="stylesheet">
<style>
  :root {
    --backdrop: #232323;
    --card: #1f1f26;
    --brand-blue: #2340a0;
    --brand-red: #c21f2a;
    --white: #ffffff;
    --text-light: #e9e9ee;
  }
  * { margin: 0; padding: 0; box-sizing: border-box; }
  html, body {
    width: 1200px; height: 780px; overflow: hidden;
    background: var(--backdrop);
    font-family: "Open Sans", Arial, sans-serif;
  }
  .canvas { position: relative; width: 1200px; height: 780px; }
  .card {
    position: absolute; top: 235px;
    width: 540px; height: 309px;
    background: var(--card);
    overflow: hidden;
    box-shadow: 0 12px 30px rgba(0,0,0,0.45);
  }
  .card--front { left: 40px; }
  .card--back { left: 620px; }
  .card-art { position: absolute; inset: 0; }

  .wordmark {
    position: absolute;
    color: var(--white);
    font-weight: 800;
    text-align: center;
    line-height: 1;
  }
  .wordmark-name, .wordmark-sub { display: block; }
  .card--front .wordmark { left: 270px; top: 20px; width: 220px; }
  .card--front .wordmark-name { font-size: 40px; letter-spacing: 2px; }
  .card--front .wordmark-sub { font-size: 19px; letter-spacing: 1px; margin-top: 4px; }
  .card--back .wordmark { left: 0; right: 0; top: 92px; }
  .card--back .wordmark-name { font-size: 88px; letter-spacing: 4px; }
  .card--back .wordmark-sub { font-size: 38px; letter-spacing: 2px; margin-top: 8px; }

  .name-bar {
    position: absolute; left: 14px; top: 108px;
    width: 8px; height: 48px; background: var(--brand-red);
  }
  .person-name {
    position: absolute; left: 30px; top: 102px;
    font-size: 30px; font-weight: 700; white-space: nowrap; line-height: 1.3;
  }
  .person-name .first { color: var(--brand-blue); }
  .person-name .last { color: var(--brand-red); }
  .license {
    position: absolute; left: 30px; top: 144px;
    font-size: 12px; color: var(--brand-red);
  }
  .license .number { color: var(--text-light); }
  .contact {
    position: absolute; left: 30px; top: 176px;
    list-style: none; font-size: 12.5px; color: var(--text-light); line-height: 1.7;
  }
  .contact li { display: flex; align-items: center; gap: 6px; }
  .contact svg { width: 11px; height: 11px; flex: none; }
</style>
</head>
<body>
<main class="canvas">

  <section class="card card--front" aria-label="Business card front">
    <svg class="card-art" viewBox="0 0 540 309">
      <defs>
        <linearGradient id="portraitTone" x1="0" y1="1" x2="0.6" y2="0">
          <stop offset="0" stop-color="#2a2a2e"/>
          <stop offset="0.45" stop-color="#6b6b70"/>
          <stop offset="0.75" stop-color="#d9d9d9"/>
          <stop offset="1" stop-color="#f4f4f4"/>
        </linearGradient>
      </defs>
      <path class="accent-blue" d="M220 309 C236 240 268 196 312 168 C282 200 258 250 240 309 Z" fill="var(--brand-blue)"/>
      <path class="accent-red" d="M306 198 C356 150 430 116 540 102 L540 114 C440 126 366 154 306 198 Z" fill="var(--brand-red)"/>
      <path class="portrait" role="img" aria-label="Portrait photo of the company owner in a dark suit and tie"
            d="M246 309 C260 252 284 212 318 188 C368 152 440 128 540 120 L540 309 Z" fill="url(#portraitTone)"/>
    </svg>

    <div class="wordmark">
      <span class="wordmark-name">K9R</span>
      <span class="wordmark-sub">CONSTRUCTION</span>
    </div>

    <div class="name-bar"></div>
    <h1 class="person-name"><span class="first">Dana</span> <span class="last">Whitfield</span></h1>
    <p class="license">MN License # <span class="number">BC482615</span></p>
    <ul class="contact">
      <li>
        <svg viewBox="0 0 24 24" aria-hidden="true"><path fill="var(--brand-red)" d="M6.6 10.8a15.1 15.1 0 0 0 6.6 6.6l2.2-2.2c.3-.3.7-.4 1-.2 1.1.4 2.3.6 3.6.6.6 0 1 .4 1 1V20c0 .6-.4 1-1 1A17 17 0 0 1 3 4c0-.6.4-1 1-1h3.5c.6 0 1 .4 1 1 0 1.3.2 2.5.6 3.6.1.3 0 .7-.2 1z"/></svg>
        612-555-0147
      </li>
      <li>
        <svg viewBox="0 0 24 24" aria-hidden="true"><rect x="2" y="5" width="20" height="14" rx="2" fill="var(--brand-blue)"/><path d="M3 6l9 7 9-7" stroke="#fff" stroke-width="1.6" fill="none"/></svg>
        dwhitfield@mailbox.com
      </li>
    </ul>
  </section>

  <section class="card card--back" aria-label="Business card back">
    <div class="wordmark">
      <span class="wordmark-name">K9R</span>
      <span class="wordmark-sub">CONSTRUCTION</span>
    </div>
  </section>

</main>
</body>
</html>
```